4"x9" Roofing Flyer Design - Tile Roofing!

We are looking to create a 4"x9" double sided flyer in full color that displays pictures of before and after of tile underlayment replacement. This would have words as well.

The theme should match the overall theme of our brochure that we already have designed so they are cohesive.

I have uploaded an example of a similar flyer that we like the overall layout of.

Please read the "Design Wording" PDF I uploaded for the words and overall design layout we are looking for on this brochure.

Please let me know if you'd like more photos or anything like that.

Target Market(s)

Retirees

Industry/Entity Type

Roofing

Font styles to use
Other font styles liked:
• Match existing fonts from our brochure

Requirements
Must have
• Must match style of existing brochure (uploaded), font must match closely as well

```html
<!DOCTYPE html>
<html lang="en">
<head>
<meta charset="utf-8">
<title>Kestrel Roofing – Tile Underlayment Flyer</title>
<link rel="stylesheet" href="https://fonts.googleapis.com/css2?family=Arimo:ital,wght@0,400;0,700;1,400;1,700&family=Roboto+Slab:wght@800&display=swap">
<style>
  :root {
    --ink: #000000;
    --paper: #ffffff;
    --orange: #e8571e;
    --photo-concrete: #8c8782;
    --photo-membrane: #c8ccd3;
    --photo-rot: #6a5848;
    --photo-tile: #a4886f;
  }
  html, body { margin: 0; padding: 0; overflow: hidden; background: var(--paper); }
  .sheet { position: relative; width: 1112px; height: 1200px; overflow: hidden; background: var(--paper); font-family: "Arimo", Arial, sans-serif; }
  .panel { position: absolute; top: 0; width: 533px; height: 1200px; background: var(--ink); overflow: hidden; }
  .panel--front { left: 0; }
  .panel--back { left: 579px; }
  .panel-art { position: absolute; left: 0; top: 0; width: 533px; height: 1200px; }

  .brand-name { position: absolute; left: 0; width: 533px; top: 106px; margin: 0; text-align: center;
    font-family: "Roboto Slab", Georgia, serif; font-weight: 800; font-size: 46px; line-height: 54px; color: var(--paper); }
  .brand-phone { position: absolute; left: 0; width: 533px; top: 168px; margin: 0; text-align: center;
    font-weight: 700; font-size: 48px; line-height: 54px; color: var(--orange); letter-spacing: -0.5px; }

  .headline { position: absolute; margin: 0; font-weight: 700; font-style: italic; font-size: 34px; line-height: 38px; white-space: nowrap; }
  .headline--white { color: var(--paper); left: 37px; top: 760px; }
  .headline--orange { color: var(--orange); left: 102px; top: 799px; }

  .copy { position: absolute; margin: 0; color: var(--paper); font-style: italic; text-align: justify; }
  .copy p { margin: 0; }
  .copy strong { color: var(--orange); font-weight: 700; }
  .copy--front { left: 28px; width: 476px; top: 842px; font-size: 14.2px; line-height: 17.7px; letter-spacing: -0.3px; }
  .copy--front p + p { margin-top: 17.7px; }
  .copy--back { left: 45px; width: 443px; top: 484px; font-size: 17.4px; line-height: 24.3px; letter-spacing: -0.2px; }
  .copy--back p + p { margin-top: 24.3px; }

  .solution-title { position: absolute; left: 0; width: 533px; top: 313px; margin: 0; text-align: center;
    color: var(--orange); font-weight: 700; font-style: italic; font-size: 38px; line-height: 44px; letter-spacing: -0.3px; }
  .solution-sub { position: absolute; left: 0; width: 533px; top: 364px; margin: 0; text-align: center;
    color: var(--paper); font-weight: 700; font-style: italic; font-size: 32.5px; line-height: 41px; }

  .footer-contact { position: absolute; left: 0; width: 533px; top: 1086px; margin: 0; text-align: center;
    color: var(--paper); font-weight: 700; font-size: 35px; line-height: 45px; }

  .tag-text { fill: var(--paper); font-family: "Arimo", Arial, sans-serif; font-weight: 700; font-style: italic; }
</style>
</head>
<body>
<main class="sheet">

  <!-- Front side -->
  <section class="panel panel--front">
    <svg class="panel-art" viewBox="0 0 533 1200" aria-hidden="false">
      <g role="img" aria-label="Before photo: cracked, decayed tile underlayment under a lifted concrete tile">
        <rect x="0" y="230" width="266" height="300" fill="var(--photo-concrete)"/>
      </g>
      <g role="img" aria-label="After photo: roof covered in new synthetic tile underlayment with battens">
        <rect x="266" y="230" width="267" height="300" fill="var(--photo-membrane)"/>
      </g>
      <g role="img" aria-label="Before photo: rotted, crumbling underlayment and debris on the roof deck">
        <polygon points="0,526 266,472 266,739 0,739" fill="var(--photo-rot)"/>
      </g>
      <g role="img" aria-label="After photo: finished roof with tiles re-laid and vents in place">
        <polygon points="266,472 533,526 533,739 266,739" fill="var(--photo-tile)"/>
      </g>

      <polygon points="0,0 533,0 533,293 266,236 0,293" fill="var(--ink)"/>
      <rect x="262" y="230" width="9" height="510" fill="var(--ink)"/>

      <polyline points="0,286 266,229 533,286" fill="none" stroke="var(--orange)" stroke-width="6"/>
      <polyline points="0,291 266,234 533,291" fill="none" stroke="var(--paper)" stroke-width="3"/>
      <polyline points="0,520 266,466 533,520" fill="none" stroke="var(--orange)" stroke-width="6"/>
      <polyline points="0,525 266,471 533,525" fill="none" stroke="var(--paper)" stroke-width="3"/>

      <g transform="translate(82 478) rotate(-16)">
        <polygon points="-62,-18 70,-18 62,18 -70,18" fill="var(--orange)"/>
        <text class="tag-text" x="-4" y="-3" font-size="11.5" text-anchor="middle">Before Decayed</text>
        <text class="tag-text" x="-4" y="12" font-size="11.5" text-anchor="middle">Tile Underlayment</text>
      </g>
      <g transform="translate(447 480) rotate(15)">
        <polygon points="-70,-18 62,-18 70,18 -62,18" fill="var(--orange)"/>
        <text class="tag-text" x="-10" y="-3" font-size="11.5" text-anchor="middle">After</text>
        <text class="tag-text" x="0" y="12" font-size="11.5" text-anchor="middle">Tile Underlayment</text>
      </g>

      <polygon points="0,704 123,704 147,739 0,739" fill="var(--orange)"/>
      <text class="tag-text" x="42" y="730" font-size="14.5">Before</text>
      <polygon points="406,704 533,704 533,739 384,739" fill="var(--orange)"/>
      <text class="tag-text" x="433" y="730" font-size="14.5">After</text>

      <rect x="0" y="1176" width="533" height="24" fill="var(--orange)"/>
    </svg>

    <h1 class="brand-name">Kestrel Roofing</h1>
    <p class="brand-phone">(555) 214-7730</p>

    <h2 class="headline headline--white">The Hidden Clock</h2>
    <h2 class="headline headline--orange">Ticking Under Your Tiles</h2>

    <div class="copy copy--front">
      <p>When a tile roof is installed, the tiles themselves are not waterproof—they are simply a shield. The actual waterproofing is done by the felt or synthetic underlayment installed beneath them.</p>
      <p>In homes of your vintage, this underlayment is now:</p>
      <p><strong>Brittle and Chalky:</strong> It cracks and turns into powder under the constant heat cycles, losing its waterproofing integrity.</p>
      <p><strong>Compromised:</strong> Even a single leak in a neighboring home means the moisture risk has increased exponentially across the entire block.</p>
      <p>Based on the age and materials used in this specific neighborhood, underlayment failure is not a matter of if, but when.</p>
      <p>Waiting for a visible ceiling stain often means the damage has already spread to the roof deck, rafters, and interior walls. A slow leak can silently cost thousands in remediation before you ever see a drop.</p>
    </div>
  </section>

  <!-- Back side -->
  <section class="panel panel--back">
    <svg class="panel-art" viewBox="0 0 533 1200" aria-hidden="true">
      <polyline points="0,286 266,229 533,286" fill="none" stroke="var(--orange)" stroke-width="6"/>
      <polyline points="0,291 266,234 533,291" fill="none" stroke="var(--paper)" stroke-width="3"/>
      <polyline points="0,1075 266,1015 533,1075" fill="none" stroke="var(--orange)" stroke-width="5"/>
      <polyline points="0,1080 266,1020 533,1080" fill="none" stroke="var(--paper)" stroke-width="3"/>
      <polygon points="0,1084 266,1024 533,1084 533,1200 0,1200" fill="var(--orange)"/>
    </svg>

    <h1 class="brand-name">Kestrel Roofing</h1>
    <p class="brand-phone">(555) 214-7730</p>

    <h2 class="solution-title">Our Certified Solution:</h2>
    <h3 class="solution-sub">The Proactive, Full-Service<br>Tile Lift &amp; Re-Lay</h3>

    <div class="copy copy--back">
      <p>We specialize in preserving your beautiful tile roof while replacing the single most important component: the underlayment.</p>
      <p>As a licensed, bonded, and insured local contractor, we don't just replace the felt; we ensure your entire roof is built to perform:</p>
      <p><strong>Careful Tile Removal:</strong> Each tile is removed by hand, inspected, and saved.</p>
      <p><strong>Deck Inspection:</strong> We check for and address any underlying damage or rot.</p>
      <p><strong>Premium Underlayment:</strong> We install a modern, high-grade self-adhered synthetic underlayment.</p>
      <p><strong>Tile Reinstallation:</strong> Your original, attractive tiles are re-laid with new flashings and seals, ready to perform for years.</p>
    </div>

    <p class="footer-contact">www.kestrel-roofing.com<br>AZ ROC 512746</p>
  </section>

</main>
</body>
</html>
```